Classic Minimalistic Business Card

Design a classic, minimalistic Business Card. Please find inspiration in the attached Classic Minimalistic examples. My information:
Name: Glen Ovamir
Company: Ovamir Capital
Logo: OC
Address: 1470 N Thornwick Rd, Suite 210 | Geneva, IL 60134
Phone: 630-555-0192
Email: glenovamir@pvt.insure
Slogan: Building Strength Through Capital

Feel free to leave out any of the information above except my name.

I have selected Double-sided, but I am also open to Single-sided

Target Market(s)

22-70. income greater than 150k/year

Industry/Entity Type

Finance

Contact Information for Business Card

See Project Description

Requirements
Must have
• Ivory or "antiqued" background similar to the reference pictures

```html
<!DOCTYPE html>
<html lang="en">
<head>
<meta charset="UTF-8">
<title>Ovamir Capital — Business Card</title>
<link rel="stylesheet" href="https://fonts.googleapis.com/css2?family=Cinzel:wght@400;600&family=Pinyon+Script&family=Yesteryear&family=Marcellus&display=swap">
<style>
  :root {
    --page: #ffffff;
    --ivory: #f6efd4;
    --ink: #121110;
  }
  html, body {
    margin: 0;
    padding: 0;
    width: 1200px;
    height: 1000px;
    overflow: hidden;
    background: var(--page);
  }
  .canvas {
    position: relative;
    width: 1200px;
    height: 1000px;
  }
  .card {
    position: absolute;
    left: 225px;
    width: 750px;
    height: 389px;
    background: var(--ivory);
    color: var(--ink);
  }
  .card--front { top: 78px; }
  .card--back  { top: 506px; }

  .monogram {
    position: absolute;
    left: 0;
    right: 0;
    text-align: center;
    font-family: "Cinzel", serif;
    font-weight: 600;
    color: var(--ink);
    line-height: 1;
  }
  .card--front .monogram {
    top: 110px;
    font-size: 150px;
    letter-spacing: -0.02em;
  }
  .card--back .monogram {
    top: 22px;
    font-size: 54px;
  }

  .identity {
    position: absolute;
    left: 0;
    right: 0;
    top: 135px;
    text-align: center;
  }
  .identity__name {
    font-family: "Pinyon Script", cursive;
    font-size: 66px;
    line-height: 1;
    margin: 0;
    font-weight: 400;
  }
  .identity__company {
    font-family: "Cinzel", serif;
    font-size: 16px;
    letter-spacing: 0.42em;
    margin: 2px 0 0 0.42em;
    line-height: 1.1;
  }
  .identity__slogan {
    font-family: "Yesteryear", cursive;
    font-size: 20px;
    margin: 0;
    line-height: 1.1;
  }

  .contact {
    position: absolute;
    top: 312px;
    font-family: "Marcellus", serif;
    text-transform: uppercase;
    line-height: 1;
  }
  .contact--left { left: 37px; }
  .contact--right { left: 447px; }
  .contact__email {
    font-size: 15px;
    letter-spacing: 0.06em;
    margin: 0 0 10px;
  }
  .contact__phone {
    font-size: 22px;
    letter-spacing: 0.03em;
    margin: 0;
  }
  .contact__street {
    font-size: 21px;
    letter-spacing: 0.12em;
    margin: 0 0 9px;
  }
  .contact__city {
    font-size: 16px;
    letter-spacing: 0.04em;
    margin: 0;
  }
</style>
</head>
<body>
<main class="canvas">
  <section class="card card--front" aria-label="Card front">
    <div class="monogram">OC</div>
  </section>

  <section class="card card--back" aria-label="Card back">
    <div class="monogram">OC</div>

    <div class="identity">
      <h1 class="identity__name">Glen Ovamir</h1>
      <p class="identity__company">OVAMIR CAPITAL</p>
      <p class="identity__slogan">Building Strength Through Capital</p>
    </div>

    <div class="contact contact--left">
      <p class="contact__email">glenovamir@pvt.insure</p>
      <p class="contact__phone">630 - 555 - 0192</p>
    </div>

    <div class="contact contact--right">
      <p class="contact__street">1470 N Thornwick Rd,</p>
      <p class="contact__city">Suite 210 | Geneva, IL 60134</p>
    </div>
  </section>
</main>
</body>
</html>
```